Brightfold Sky Advisors needs a wordpress design

New consulting company based in San Francisco focusing on leading businesses (primarily startups) into the cloud. Services include: cloud architecture, security, automation, back-end design, Infrastructure Optimization, Capacity Planning. Even though we are a new company, I'd like to convey a sense of confidence to the prospective client. Logos are attached

Target Market(s)

Start-ups looking to move their application into the cloud

Industry/Entity Type

Information Technology

```html
<!DOCTYPE html>
<html lang="en">
<head>
<meta charset="utf-8">
<title>Brightfold Sky Advisors</title>
<link href="https://fonts.googleapis.com/css2?family=Raleway:wght@400;500;600;700&family=Open+Sans:wght@400;600&display=swap" rel="stylesheet">
<style>
:root{
  --blue:#1d86d0;
  --blue-dark:#1570b3;
  --heading:#2a8fd6;
  --text:#555b61;
  --white:#ffffff;
  --night:#1b2431;
  --night-2:#2f3b4c;
  --line:#d9dde1;
  --hero-top:#93a9bb;
  --hero-mid:#a9987c;
  --hero-bottom:#6d604b;
}
*{margin:0;padding:0;box-sizing:border-box}
html,body{width:786px;height:1200px;overflow:hidden}
body{position:relative;font-family:'Open Sans',sans-serif;color:var(--text);background:var(--white)}

.hero{position:relative;height:340px;overflow:hidden}
.hero-photo{position:absolute;inset:0;background:linear-gradient(180deg,var(--hero-top) 0%,var(--hero-mid) 55%,var(--hero-bottom) 100%)}
.site-header{position:absolute;top:0;left:0;right:0;display:flex;justify-content:space-between;align-items:flex-start;padding:12px 28px 0 30px}
.brand{display:flex;align-items:center;gap:8px;font-family:'Raleway',sans-serif;font-weight:700;font-size:13px;color:var(--blue-dark);background:rgba(255,255,255,.92);padding:7px 10px;border-radius:3px}
.brand-dot{width:16px;height:16px;border-radius:50%;background:var(--blue)}
.main-nav{display:flex;gap:4px;font-family:'Raleway',sans-serif;font-size:10px;font-weight:600}
.main-nav a{color:var(--white);text-decoration:none;padding:7px 9px}
.main-nav a.active{background:var(--blue);border-radius:2px}
.hero-caption{position:absolute;left:0;right:0;top:245px;text-align:center}
.hero-caption h1{font-family:'Raleway',sans-serif;font-weight:500;font-size:17px;color:var(--white);text-shadow:0 1px 3px rgba(0,0,0,.4)}
.btn-more{display:inline-block;margin-top:10px;padding:6px 14px;border:1px solid var(--white);color:var(--white);font-size:9px;letter-spacing:1px;font-family:'Raleway',sans-serif;font-weight:600;background:rgba(0,0,0,.25)}
.slider-dots{display:flex;justify-content:center;gap:5px;margin-top:10px}
.slider-dots span{width:6px;height:6px;border-radius:50%;background:rgba(255,255,255,.55)}
.slider-dots span.on{background:var(--white)}

.section-title{font-family:'Raleway',sans-serif;font-weight:500;font-size:22px;color:var(--heading);text-align:center;letter-spacing:.5px}
.services{padding-top:44px}
.service-grid{display:grid;grid-template-columns:repeat(3,226px);gap:20px 22px;justify-content:center;margin-top:20px}
.service-card{position:relative;height:131px;background:var(--blue);color:var(--white);text-align:center;padding:13px 16px 0;border-radius:2px}
.service-card svg.icon{width:24px;height:24px;display:block;margin:0 auto 5px}
.service-card h3{font-family:'Raleway',sans-serif;font-size:11px;font-weight:700;margin-bottom:5px}
.service-card p{font-size:7.5px;line-height:1.45;opacity:.92}
.card-more{position:absolute;left:50%;bottom:8px;width:14px;height:14px;margin-left:-7px;border-radius:50%;background:var(--white)}

.partners{padding-top:44px}
.partner-row{display:flex;justify-content:center;gap:44px;margin-top:16px;font-family:'Raleway',sans-serif;font-weight:700;font-size:12px;color:#444a50}

.testimonials{position:absolute;top:872px;left:0;right:0;height:241px;background:linear-gradient(180deg,var(--night-2) 0%,var(--night) 60%,#131a24 100%);color:var(--white)}
.testimonials .section-title{color:var(--white);padding-top:20px}
.quote{position:absolute;left:128px;top:80px;display:flex;gap:24px;width:585px}
.client-photo{flex:0 0 90px;height:90px;border-radius:50%;border:3px solid var(--white);background:linear-gradient(160deg,#b9c3cc,#6f7d8a)}
.quote-body{position:relative;padding-left:34px;padding-top:2px}
.quote-mark{position:absolute;left:0;top:-8px;font-family:'Raleway',sans-serif;font-size:44px;font-weight:700;line-height:1}
.quote-body h4{font-family:'Raleway',sans-serif;font-size:17px;font-weight:500;margin-bottom:6px}
.quote-body p{font-size:8px;line-height:1.55;opacity:.85}
.arrow{position:absolute;top:112px;width:14px;height:14px}
.arrow.prev{left:22px}.arrow.next{right:22px}

.site-footer{position:absolute;top:1113px;left:0;right:0;height:87px;text-align:center}
.social{display:flex;justify-content:center;gap:6px;padding-top:12px}
.social span{width:16px;height:16px;border-radius:50%;border:1px solid var(--blue)}
.footer-nav{display:flex;justify-content:center;gap:14px;margin-top:10px;font-size:7.5px;color:var(--text)}
.footer-nav span{color:var(--line)}
.copyright{font-size:7px;margin-top:6px;color:#7a8086}
</style>
</head>
<body>

<section class="hero">
  <div class="hero-photo" role="img" aria-label="Photo of a red suspension bridge over the bay at sunrise"></div>
  <header class="site-header">
    <div class="brand"><span class="brand-dot"></span>Brightfold Sky Advisors</div>
    <nav class="main-nav">
      <a class="active" href="#">Home</a><a href="#">About Us</a><a href="#">Our Services</a><a href="#">Clients</a><a href="#">FAQs</a><a href="#">Contact Us</a>
    </nav>
  </header>
  <div class="hero-caption">
    <h1>We Provide Cloud Consulting Services</h1>
    <span class="btn-more">LEARN MORE</span>
    <div class="slider-dots"><span class="on"></span><span></span><span></span><span></span></div>
  </div>
</section>

<section class="services">
  <h2 class="section-title">OUR SERVICES</h2>
  <div class="service-grid">
    <article class="service-card">
      <svg class="icon" viewBox="0 0 24 24" fill="#fff"><path d="M7 19a5 5 0 0 1-.6-9.96A6 6 0 0 1 18 9.5a4.75 4.75 0 0 1-.5 9.5z"/></svg>
      <h3>Cloud Architecture</h3>
      <p>We design scalable cloud platforms that grow with your product, keeping costs clear and performance steady from day one.</p>
      <span class="card-more"></span>
    </article>
    <article class="service-card">
      <svg class="icon" viewBox="0 0 24 24" fill="#fff"><path d="M12 2l8 3v6c0 5-3.4 9.4-8 11-4.6-1.6-8-6-8-11V5z"/></svg>
      <h3>Security</h3>
      <p>We harden every layer of your stack with access controls, encryption and monitoring so your data stays safe and private.</p>
      <span class="card-more"></span>
    </article>
    <article class="service-card">
      <svg class="icon" viewBox="0 0 24 24" fill="none" stroke="#fff" stroke-width="2"><rect x="3" y="4" width="18" height="12" rx="1"/><path d="M9 20h6M12 16v4"/></svg>
      <h3>Automation</h3>
      <p>We script builds, tests and deployments so your team ships faster with fewer errors and far less manual work each week.</p>
      <span class="card-more"></span>
    </article>
    <article class="service-card">
      <svg class="icon" viewBox="0 0 24 24" fill="none" stroke="#fff" stroke-width="2"><path d="M4 20l4-1L19 8l-3-3L5 16zM14 7l3 3"/></svg>
      <h3>Back-End Design</h3>
      <p>We build reliable APIs, queues and databases that handle real traffic and keep your application responsive under heavy load.</p>
      <span class="card-more"></span>
    </article>
    <article class="service-card">
      <svg class="icon" viewBox="0 0 24 24" fill="none" stroke="#fff" stroke-width="2"><rect x="5" y="3" width="14" height="18" rx="1"/><path d="M8 8h8M8 12h8M8 16h5"/></svg>
      <h3>Infrastructure Optimization</h3>
      <p>We review your current servers and services, remove waste and tune settings to get more from every dollar you spend.</p>
      <span class="card-more"></span>
    </article>
    <article class="service-card">
      <svg class="icon" viewBox="0 0 24 24" fill="none" stroke="#fff" stroke-width="2"><rect x="3" y="5" width="14" height="15" rx="1"/><path d="M10 14l9-9 2 2-9 9-3 1z"/></svg>
      <h3>Capacity Planning</h3>
      <p>We forecast growth from your usage data and plan resources ahead, so launches and traffic spikes never catch you off guard.</p>
      <span class="card-more"></span>
    </article>
  </div>
</section>

<section class="partners">
  <h2 class="section-title">PARTNERS LOGOS</h2>
  <div class="partner-row">
    <span>Norvale</span><span>Bexley</span><span>Trentham</span><span>Orvanta</span><span>Kestrel Point</span><span>Fizzwell</span>
  </div>
</section>

<section class="testimonials">
  <h2 class="section-title">TESTIMONIALS</h2>
  <svg class="arrow prev" viewBox="0 0 14 14" fill="none" stroke="#fff" stroke-width="2"><path d="M9 2L4 7l5 5"/></svg>
  <div class="quote">
    <div class="client-photo" role="img" aria-label="Portrait photo of the client"></div>
    <div class="quote-body">
      <span class="quote-mark">&ldquo;</span>
      <h4>Daniel Hartwell</h4>
      <p>Brightfold moved our whole platform to the cloud in six weeks. Their team was calm, clear and always ahead of the next problem. Our costs dropped and our uptime has never been better.</p>
    </div>
  </div>
  <svg class="arrow next" viewBox="0 0 14 14" fill="none" stroke="#fff" stroke-width="2"><path d="M5 2l5 5-5 5"/></svg>
</section>

<footer class="site-footer">
  <div class="social"><span></span><span></span><span></span><span></span></div>
  <nav class="footer-nav">
    <a>Home</a><span>|</span><a>About Us</a><span>|</span><a>Our Services</a><span>|</span><a>Clients</a><span>|</span><a>FAQs</a><span>|</span><a>Contact Us</a>
  </nav>
  <p class="copyright">&copy; 2014 Brightfold Sky Advisors. All Rights Reserved</p>
</footer>

</body>
</html>
```